Corporate Identity Pack - LetterHead, Business Card, Envelope

We are looking for a clean, professional, and visually connected corporate identity set for our company "MERIDA CARE" (Cleaning, Gardening, and Pest Control services).

The pack must include:

Business Card (front and back)
Envelope with recipient window on the right side (22x11)
A4 Letterhead

We provide:
Our final logo (PNG)
Three design references (Inspiration1, Inspiration2, Inspiration3) to spark ideas — but you are absolutely free to propose your own creative solutions based on these concepts.

What we want:
A clean, modern, and trustworthy style
A subtle but creative watermark or graphic detail on the letterhead (not too invasive)

The same visual "family feeling" across business card, envelope, and letterhead: designs must be different but clearly connected

Strong readability for all text and contact details

Use our brand colors (Navy Blue, Green, Orange/Red) in a smart, non-overloaded way

No strict limitations: we are open to creative proposals as long as they are coherent, elegant, and suitable for professional use

Technical specifications:
100% full A4 page layout (no accidental borders)

Deliver ready-to-print PDFs and vector files (AI, EPS)

Respect 5 mm safety margins

Standard sizes for A4, business card, envelope C6 with window at the right

Tone:
Modern – Clean – Elegant – Creative – Trustworthy

Target Market(s)

Professional businesses, property managers, condominium administrators, companies, clinics, and offices requiring cleaning, gardening, and pest control services. The design must convey trust, reliability, professionalism, and attention to detail.

Industry/Entity Type

Cleaning Services, Gardening Services, Pest Control Services

Colors
0054AA
0677BA
7BADD7
CADEEF
E8F1F8
59FF00
82FF00
B8FF75
E3FFCB
F4FFEA
EB3D1F
EC4F4E
F09395
F8D3D4
FCEDEE

Requirements
Must have
• Cohesive design across business card, letterhead, and envelope Clean, modern, professional look Use of brand colors: Navy Blue (main), Green, Orange/Red accents Letterhead must include a subtle watermark without interfering with text Envelope must be with a transparent window for recipient address visibility High readability of all text and contact details Proper alignment, no unnecessary margins (full A4 layout)
Nice to have
• Creative but discreet use of the checkmark from the logo as part of the background or watermark Slight variation or accent of color tones while respecting brand identity A clean visual accent that gives a sense of movement or dynamic professionalism (without being distracting) Icons for email, phone, and website on the business card (if stylistically appropriate)
Should not have
• Overuse of colors or rainbow effects Heavy backgrounds or complex textures that interfere with readability Fonts that are too playful, comic-style, or non-professional Overcrowded layouts — the design must feel clean and spacious Watermarks that are too strong or central (they must be subtle and marginal)

```html
<!DOCTYPE html>
<html lang="en">
<head>
<meta charset="utf-8">
<title>MERIDA CARE – Corporate Identity</title>
<link href="https://fonts.googleapis.com/css2?family=Poppins:wght@300;400;500;600;700&display=swap" rel="stylesheet">
<style>
  :root{
    --navy:#211d6e;
    --green:#6fd13a;
    --orange:#f05a1e;
    --paper:#f7f7f7;
    --ink:#1f1d3f;
    --window:#e2eef4;
    --backdrop:#d6ece6;
    --watermark:rgba(33,29,110,.045);
  }
  *{box-sizing:border-box;margin:0;padding:0}
  html,body{width:1200px;height:965px;overflow:hidden}
  body{background:var(--backdrop);font-family:"Poppins",sans-serif;color:var(--ink);position:relative}
  .piece{position:absolute;overflow:hidden}
  .icon{width:1em;height:1em;fill:currentColor;vertical-align:-0.12em}

  .brand{display:flex;align-items:center;gap:.35em;white-space:nowrap}
  .brand-square{width:1.05em;height:1.05em;background:var(--green);flex:none}
  .brand-name{font-weight:600;letter-spacing:.01em;line-height:1}
  .brand-tagline{font-weight:500;letter-spacing:.09em;line-height:1;white-space:nowrap}

  /* Letterhead */
  .letterhead{left:40px;top:223px;width:480px;height:678px;background:var(--paper)}
  .letterhead .top-band{position:absolute;left:0;top:0}
  .letterhead .watermark{position:absolute;right:0;top:360px}
  .letterhead .brand{position:absolute;left:20px;top:34px;font-size:22px}
  .letterhead .brand-name{color:var(--navy)}
  .icon-rail{position:absolute;left:22px;top:573px;width:17px;height:96px;background:var(--navy);border-radius:4px;color:#fff;font-size:7px;display:flex;flex-direction:column;align-items:center;padding-top:13px;gap:14px}
  .lh-contacts{position:absolute;left:50px;top:583px;font-size:8px;line-height:1.1}
  .lh-contacts p{margin-bottom:8px}
  .lh-contacts p.tight{margin-bottom:0}
  .lh-contacts p.gap{margin-top:7px}
  .legal{font-size:8px;line-height:1.15;display:grid;grid-template-columns:auto auto;column-gap:4px;white-space:nowrap}
  .legal b{font-weight:600}
  .lh-legal-a{position:absolute;left:221px;top:621px}
  .lh-legal-b{position:absolute;left:362px;top:621px}
  .letterhead .bottom-band{position:absolute;left:0;bottom:0}

  /* Envelope back */
  .envelope-back{left:554px;top:25px;width:598px;height:323px;background:var(--navy)}
  .envelope-flap{position:absolute;left:3px;top:0;width:592px;height:89px;background:var(--green);border-radius:0 0 14px 14px}
  .envelope-back .lockup{position:absolute;left:151px;top:190px}
  .envelope-back .brand{font-size:38px;color:#fff}
  .envelope-back .brand-square{width:42px;height:42px}
  .envelope-back .brand-tagline{color:#fff;font-size:10.5px;margin:4px 0 0 58px}

  /* Envelope front */
  .envelope-front{left:554px;top:379px;width:599px;height:343px;background:var(--paper)}
  .sender{position:absolute;left:21px;top:14px;border-left:5px solid var(--navy);padding:4px 0 20px 9px;font-size:13px;line-height:1.25;font-weight:400;font-style:normal}
  .envelope-front .lockup{position:absolute;right:20px;top:20px;text-align:right}
  .envelope-front .brand{font-size:21px;justify-content:flex-end}
  .envelope-front .brand-name{color:var(--navy)}
  .envelope-front .brand-tagline{font-size:6.5px;color:var(--navy);margin-top:3px}
  .address-window{position:absolute;right:21px;top:115px;width:245px;height:92px;background:var(--window);border-radius:12px}
  .env-contacts{position:absolute;left:21px;top:240px;font-size:11px;line-height:1}
  .env-contacts li{list-style:none;margin-bottom:9px;display:flex;gap:6px;align-items:center}
  .env-contacts .icon{color:var(--navy);font-size:10px}
  .env-legal{position:absolute;right:10px;top:270px;font-size:10.5px;display:grid;grid-template-columns:auto auto;column-gap:12px;line-height:1.35;white-space:nowrap}
  .env-legal b{font-weight:600}
  .envelope-front .bottom-band{position:absolute;left:0;bottom:0}

  /* Business cards */
  .card-front{left:607px;top:754px;width:213px;height:139px;background:var(--navy)}
  .card-front .lockup{position:absolute;left:36px;top:56px}
  .card-front .brand{font-size:20px;color:#fff}
  .card-front .brand-tagline{font-size:5.2px;color:#fff;margin:3px 0 0 28px}
  .card-back{left:867px;top:754px;width:214px;height:139px;background:#fff}
  .card-back .brand{position:absolute;right:14px;top:14px;font-size:12.5px}
  .card-back .brand-name{color:var(--navy)}
  .card-contacts{position:absolute;left:14px;top:54px;font-size:5.6px;line-height:1.2}
  .card-contacts li{list-style:none;display:flex;gap:3px;align-items:center;margin-bottom:2.4px}
  .card-contacts .icon{color:var(--navy);font-size:5px}
  .card-contacts .addr{margin:1px 0 3px}
  .card-legal{font-size:5.6px}
  .card-legal.a{position:absolute;left:14px;top:104px}
  .card-legal.b{position:absolute;left:127px;top:104px}
  .card-back .bottom-band{position:absolute;left:0;bottom:0}
</style>
</head>
<body>

<svg width="0" height="0" style="position:absolute" aria-hidden="true">
  <symbol id="i-phone" viewBox="0 0 24 24"><path d="M6.6 10.8a15.1 15.1 0 0 0 6.6 6.6l2.2-2.2a1 1 0 0 1 1-.25 11.4 11.4 0 0 0 3.6.57 1 1 0 0 1 1 1V20a1 1 0 0 1-1 1A17 17 0 0 1 3 4a1 1 0 0 1 1-1h3.5a1 1 0 0 1 1 1c0 1.25.2 2.45.57 3.57a1 1 0 0 1-.25 1z"/></symbol>
  <symbol id="i-mail" viewBox="0 0 24 24"><path d="M2 5h20v14H2zm2 2v.4l8 5.2 8-5.2V7zm0 2.8V17h16V9.8l-8 5.2z"/></symbol>
  <symbol id="i-globe" viewBox="0 0 24 24"><path d="M12 2a10 10 0 1 0 0 20 10 10 0 0 0 0-20zm6.9 6h-2.9a15.7 15.7 0 0 0-1.4-3.6A8 8 0 0 1 18.9 8zM12 4c.8 1.2 1.5 2.5 1.9 4h-3.8c.4-1.5 1.1-2.8 1.9-4zM4.3 14a8.2 8.2 0 0 1 0-4h3.4a16.5 16.5 0 0 0 0 4zm.8 2h2.9c.3 1.3.8 2.5 1.4 3.6A8 8 0 0 1 5.1 16zM8 8H5.1a8 8 0 0 1 4.3-3.6C8.8 5.5 8.3 6.7 8 8zm4 12c-.8-1.2-1.5-2.5-1.9-4h3.8c-.4 1.5-1.1 2.8-1.9 4zm2.3-6H9.7a14.7 14.7 0 0 1 0-4h4.6a14.7 14.7 0 0 1 0 4zm.3 5.6c.6-1.1 1.1-2.3 1.4-3.6h2.9a8 8 0 0 1-4.3 3.6zm1.7-5.6a16.5 16.5 0 0 0 0-4h3.4a8.2 8.2 0 0 1 0 4z"/></symbol>
  <symbol id="i-pin" viewBox="0 0 24 24"><path d="M12 2a7 7 0 0 0-7 7c0 5.2 7 13 7 13s7-7.8 7-13a7 7 0 0 0-7-7zm0 9.5A2.5 2.5 0 1 1 12 6.5a2.5 2.5 0 0 1 0 5z"/></symbol>
</svg>

<!-- A4 letterhead -->
<section class="piece letterhead" aria-label="Letterhead">
  <svg class="top-band" width="480" height="20" viewBox="0 0 480 20">
    <rect width="480" height="10" fill="var(--navy)"/>
    <path d="M357 10H480V19H366Q360 19 357 10Z" fill="var(--orange)"/>
  </svg>
  <svg class="watermark" width="170" height="200" viewBox="0 0 170 200" aria-hidden="true">
    <path d="M170 0V60L40 200H0Z" fill="var(--watermark)"/>
    <path d="M170 90V140L115 200H70Z" fill="var(--watermark)"/>
  </svg>
  <div class="brand"><span class="brand-square"></span><span class="brand-name">MERIDA CARE</span></div>

  <div class="icon-rail">
    <svg class="icon"><use href="#i-phone"/></svg>
    <svg class="icon"><use href="#i-globe"/></svg>
    <svg class="icon"><use href="#i-pin"/></svg>
  </div>
  <div class="lh-contacts">
    <p>+39 345 2091736</p>
    <p class="tight">office@merida-care.srl</p>
    <p>www.merida-care.srl</p>
    <p class="gap tight">Via dei Tigli - Lindenweg 24</p>
    <p class="tight">I-39100 Valverde-Grünthal (Bz)</p>
  </div>
  <div class="legal lh-legal-a"><b>PES :</b><span>info.meridacare@pec.it</span><b>SDI :</b><span>K7TRWQ4</span></div>
  <div class="legal lh-legal-b"><b>REA -</b><span>VWV Nr. Bz 315082</span><b>P.I.&nbsp; -</b><span>MwSt. 04718350926</span></div>

  <svg class="bottom-band" width="480" height="34" viewBox="0 0 480 34">
    <path d="M0 10H226L220 17H0Z" fill="var(--green)"/>
    <path d="M240 0H480V34H40L49 24H223Q228 24 231 20L238 2Z" fill="var(--navy)"/>
  </svg>
</section>

<!-- Envelope back -->
<section class="piece envelope-back" aria-label="Envelope back">
  <div class="envelope-flap"></div>
  <div class="lockup">
    <div class="brand"><span class="brand-square"></span><span class="brand-name">MERIDA CARE</span></div>
    <p class="brand-tagline">CLEANING·GARDENING·PESTCONTROL</p>
  </div>
</section>

<!-- Envelope front -->
<section class="piece envelope-front" aria-label="Envelope front">
  <address class="sender">Via dei Tigli - Lindenweg 24<br>I-39100 Valverde-Grünthal (Bz)</address>
  <div class="lockup">
    <div class="brand"><span class="brand-square"></span><span class="brand-name">MERIDA CARE</span></div>
    <p class="brand-tagline">CLEANING·GARDENING·PESTCONTROL</p>
  </div>
  <div class="address-window"></div>
  <ul class="env-contacts">
    <li><svg class="icon"><use href="#i-phone"/></svg>+39 345 2091736</li>
    <li><svg class="icon"><use href="#i-mail"/></svg>office@merida-care.srl</li>
    <li><svg class="icon"><use href="#i-globe"/></svg>www.merida-care.srl</li>
  </ul>
  <div class="env-legal">
    <span><b>REA</b> - VWV Nr. Bz 315082</span><span><b>P.I.</b> - MwSt. 04718350926</span>
    <span><b>PES</b> : info.meridacare@pec.it</span><span><b>SDI</b> : K7TRWQ4</span>
  </div>
  <svg class="bottom-band" width="599" height="43" viewBox="0 0 599 43">
    <path d="M0 13H335L328 20H0Z" fill="var(--green)"/>
    <path d="M356 0H599V43H0V23H330Q336 23 340 18L352 3Z" fill="var(--navy)"/>
  </svg>
</section>

<!-- Business card front -->
<section class="piece card-front" aria-label="Business card front">
  <div class="lockup">
    <div class="brand"><span class="brand-square"></span><span class="brand-name">MERIDA CARE</span></div>
    <p class="brand-tagline">CLEANING·GARDENING·PESTCONTROL</p>
  </div>
</section>

<!-- Business card back -->
<section class="piece card-back" aria-label="Business card back">
  <div class="brand"><span class="brand-square"></span><span class="brand-name">MERIDA CARE</span></div>
  <ul class="card-contacts">
    <li><svg class="icon"><use href="#i-phone"/></svg>+39 345 2091736</li>
    <li><svg class="icon"><use href="#i-mail"/></svg>office@merida-care.srl</li>
    <li><svg class="icon"><use href="#i-globe"/></svg>www.merida-care.srl</li>
    <li class="addr">Via dei Tigli - Lindenweg 24<br>I-39100 Valverde-Grünthal (Bz)</li>
  </ul>
  <div class="legal card-legal a"><b>PES :</b><span>info.meridacare@pec.it</span><b>SDI :</b><span>K7TRWQ4</span></div>
  <div class="legal card-legal b"><b>REA -</b><span>VWV Nr. Bz 315082</span><b>P.I.&nbsp; -</b><span>MwSt. 04718350926</span></div>
  <svg class="bottom-band" width="214" height="17" viewBox="0 0 214 17">
    <path d="M0 4H112L108 8H0Z" fill="var(--green)"/>
    <path d="M120 0H214V17H0V11H108Q111 11 113 8L118 1Z" fill="var(--navy)"/>
  </svg>
</section>

</body>
</html>
```